KVT Building And Maintenance

Need a very professional looking double sided Buisiness card with all my details phone number, name, email, license number.

Target Market(s)

construction industry

Industry/Entity Type

building

Contact Information for Business Card

Name Dale Pemberton. Email Address Info@KVTBuilding.com.au mobile number 0452918736 licence number 671093D. web site

```html
<!DOCTYPE html>
<html lang="en">
<head>
<meta charset="utf-8">
<title>KVT Building And Maintenance – Business Card</title>
<link rel="stylesheet" href="https://fonts.googleapis.com/css2?family=Questrial&display=swap">
<style>
  :root {
    --backdrop: #8e8e8e;
    --card-white: #ffffff;
    --brand-blue: #0a95dd;
    --charcoal: #3b3b3d;
    --text-grey: #555559;
    --rule-grey: #9a9a9a;
    --back-dark: #262628;
    --back-mid: #353537;
    --back-light: #4a4a4c;
  }
  * { box-sizing: border-box; margin: 0; padding: 0; }
  html, body {
    width: 1200px; height: 800px; overflow: hidden;
    background: var(--backdrop);
    font-family: "Questrial", sans-serif;
  }
  .sheet {
    width: 1200px; height: 800px;
    display: flex; flex-direction: column;
    align-items: center; justify-content: center; gap: 28px;
  }
  .card {
    position: relative;
    width: 620px; height: 354px;
    overflow: hidden;
    box-shadow: 0 6px 18px rgba(0,0,0,0.25);
  }

  /* Front */
  .card-front { background: var(--card-white); }
  .front-bands { position: absolute; inset: 0; width: 100%; height: 100%; }
  .brand-block {
    position: absolute; left: 178px; top: 178px; width: 170px;
    color: var(--brand-blue);
    text-align: center;
  }
  .brand-name-main { display: block; font-size: 54px; line-height: 1; letter-spacing: 2px; }
  .brand-name-sub { display: block; font-size: 10.5px; letter-spacing: 1.6px; text-transform: uppercase; margin-top: 6px; }
  .divider {
    position: absolute; left: 362px; top: 176px;
    width: 1px; height: 96px; background: var(--rule-grey);
  }
  .contact {
    position: absolute; left: 380px; top: 170px;
    color: var(--text-grey); font-size: 13px; line-height: 1.5;
  }
  .contact-name {
    color: var(--brand-blue); font-size: 19px; letter-spacing: 1px;
    text-transform: uppercase; margin-bottom: 4px; line-height: 1.2;
  }
  .contact-row { display: flex; align-items: center; gap: 7px; }
  .contact-icon { width: 10px; height: 10px; flex: none; }
  .contact-licence { padding-left: 0; }

  /* Back */
  .card-back { background: var(--back-dark); }
  .back-pattern {
    position: absolute; inset: 0;
    background: linear-gradient(120deg, var(--back-light) 0%, var(--back-mid) 40%, var(--back-dark) 100%);
  }
  .back-mark {
    position: absolute; left: 470px; top: 212px;
    color: var(--card-white); font-size: 22px; letter-spacing: 1px;
  }
</style>
</head>
<body>
<main class="sheet">

  <section class="card card-front" aria-label="Business card front">
    <svg class="front-bands" viewBox="0 0 620 354" preserveAspectRatio="none" aria-hidden="true">
      <polygon fill="var(--brand-blue)" points="0,0 620,0 620,34 262,106 110,354 0,354"/>
      <polygon fill="var(--charcoal)" points="620,42 620,50 270,122 126,354 116,354 264,114"/>
    </svg>

    <div class="brand-block">
      <span class="brand-name-main">KVT</span>
      <span class="brand-name-sub">Building And Maintenance</span>
    </div>

    <div class="divider"></div>

    <div class="contact">
      <p class="contact-name">Dale Pemberton</p>
      <p class="contact-row">
        <svg class="contact-icon" viewBox="0 0 10 10" aria-hidden="true"><path fill="var(--brand-blue)" d="M2 0.5 L3.6 0.5 L4.2 2.8 L3 3.6 Q4 6 6.4 7 L7.2 5.8 L9.5 6.4 L9.5 8 Q9 9.5 7.5 9.5 Q0.5 8.5 0.5 2.5 Q0.5 1 2 0.5Z"/></svg>
        <span>0452918736</span>
      </p>
      <p class="contact-row">
        <svg class="contact-icon" viewBox="0 0 10 10" aria-hidden="true"><rect x="0.5" y="2" width="9" height="6.5" fill="var(--brand-blue)"/><polyline points="0.8,2.3 5,5.6 9.2,2.3" fill="none" stroke="#fff" stroke-width="0.9"/></svg>
        <span>Info@KVTBuilding.com.au</span>
      </p>
      <p class="contact-row">
        <svg class="contact-icon" viewBox="0 0 10 10" aria-hidden="true"><circle cx="5" cy="5" r="4.5" fill="var(--brand-blue)"/><ellipse cx="5" cy="5" rx="1.8" ry="4.3" fill="none" stroke="#fff" stroke-width="0.7"/><line x1="0.6" y1="5" x2="9.4" y2="5" stroke="#fff" stroke-width="0.7"/></svg>
        <span>KVTBuilding.com.au</span>
      </p>
      <p class="contact-licence">Licence NO: 671093D</p>
    </div>
  </section>

  <section class="card card-back" aria-label="Business card back">
    <div class="back-pattern" role="img" aria-label="Tone-on-tone repeating brand pattern in dark charcoal"></div>
    <span class="back-mark">KVT Building And Maintenance</span>
  </section>

</main>
</body>
</html>
```